Quiet Harbour is a Counseling company and needs a website design.

I need a website design for my Counseling company based in Singapore. I provide counseling and other related services through therapy. I website is my front face and want it to represent my personality and the name of the company itself. My company represents non judgement, compassionate and a safe environment for people to come by and talk about their issues/problems.

I want the website to be something connected to nature earth like a perfect Sanctuary. When a person sees my website i want to immediately feel a piece of calmness and peace. This is essential to me.

Target Market(s)

All age groups above 13 years of age

Industry/Entity Type

It Company

Requirements
Must have
• Not too flashy and must connect to any common man irrespective of age
Should not have
• Good calm color concept

```html
<!DOCTYPE html>
<html lang="en">
<head>
<meta charset="utf-8">
<title>Quiet Harbour — Integrating into new Culture</title>
<link rel="stylesheet" href="https://fonts.googleapis.com/css2?family=Cutive+Mono&display=swap">
<style>
  :root {
    --ink: #ffffff;
    --ink-soft: #e8e4de;
    --bar: rgba(20, 12, 10, 0.62);
    --panel: rgba(14, 12, 14, 0.72);
    --menu: rgba(12, 12, 16, 0.82);
    --band: rgba(8, 8, 12, 0.45);
    --tone-top: #3a1c16;
    --tone-mid: #122058;
    --tone-low: #2a1620;
    --tone-water: #3a2014;
    --dot: #9a9aa2;
    --dot-active: #1a1a1e;
  }
  * { margin: 0; padding: 0; box-sizing: border-box; }
  html, body { width: 1200px; height: 775px; overflow: hidden; background: #000; }
  body {
    position: relative;
    font-family: "Cutive Mono", "Courier New", monospace;
    font-variant: small-caps;
    color: var(--ink);
  }
  .scene {
    position: absolute; inset: 0;
    background: linear-gradient(180deg, var(--tone-top) 0%, var(--tone-mid) 45%, var(--tone-low) 62%, var(--tone-water) 100%);
  }
  .topbar {
    position: absolute; left: 0; top: 0; width: 1200px; height: 47px;
    background: var(--bar);
  }
  .brand {
    position: absolute; left: 47px; top: 15px;
    font-size: 15px; letter-spacing: 0.5px;
  }
  .nav {
    position: absolute; right: 51px; top: 15px;
    display: flex; gap: 8px; font-size: 15px; list-style: none;
  }
  .nav .sep { color: var(--ink-soft); }
  .nav .current { text-decoration: underline; text-underline-offset: 3px; }
  .submenu {
    position: absolute; left: 861px; top: 47px; width: 248px; height: 74px;
    background: var(--menu); padding: 7px 12px; list-style: none;
    font-size: 13px; line-height: 17px;
  }
  .submenu .active { text-decoration: underline; text-underline-offset: 3px; }
  .article {
    position: absolute; left: 154px; top: 148px; width: 545px; height: 534px;
    background: var(--panel); padding: 20px 26px 0 26px;
  }
  .article h1 {
    font-weight: 400; font-size: 28px; letter-spacing: 1.8px; margin: 0 0 26px 0;
  }
  .article p {
    font-size: 16px; line-height: 26px; text-indent: 20px; margin-bottom: 26px;
    letter-spacing: 2px;
  }
  .slides {
    position: absolute; top: 705px; left: 935px; display: flex; gap: 11px;
  }
  .slides span { width: 8px; height: 8px; border-radius: 50%; background: var(--dot); }
  .slides span.on { background: var(--dot-active); border: 1px solid var(--dot); }
  .footer-band {
    position: absolute; left: 0; bottom: 0; width: 1200px; height: 46px;
    background: var(--band);
  }
</style>
</head>
<body>
  <div class="scene" role="img" aria-label="Night view of a city waterfront with a lit bridge, skyline and colourful reflections on the water"></div>

  <header class="topbar">
    <div class="brand">Quiet Harbour</div>
    <ul class="nav">
      <li>Home</li><li class="sep">/</li>
      <li>About</li><li class="sep">/</li>
      <li class="current">Consultation</li><li class="sep">/</li>
      <li>Resources</li><li class="sep">/</li>
      <li>Contact</li>
    </ul>
  </header>

  <ul class="submenu">
    <li class="active">-Integrating into new culture</li>
    <li>-Better balanced life</li>
    <li>-My working Model</li>
  </ul>

  <main class="article">
    <h1>Integrating into new Culture</h1>
    <p>Lorem ipsum dolor sit amet, consectetur adipiscing elit. Praesent ullamcorper interdum faucibus. Aenean vel tellus porta, luctus urna eu, ornare felis. Nulla accumsan, nisi in sodales faucibus, elit neque scelerisque sem, elementum interdum enim dui vitae justo. In commodo ipsum in vestibulum pretium. In non nisi enim. Ut laoreet sapien nisi, sed dapibus lectus porttitor vitae.</p>
    <p>Aliquam sagittis enim sodales, venenatis nibh ac, imperdiet justo. Nullam dolor nisi, viverra ac pretium sed, pulvinar eu neque. Curabitur mattis metus eros. Aenean faucibus, magna eget porttitor suscipit, mauris nisi semper lectus, dictum elementum metus elit vitae turpis. Nulla sed ante gravida, pharetra augue in, volutpat metus.</p>
  </main>

  <div class="slides" aria-label="Slide selector">
    <span class="on"></span><span></span><span></span><span></span><span></span>
  </div>

  <div class="footer-band"></div>
</body>
</html>
```